Seeds of Renewal needs a business card design

I need a business card design for my company to promote my new Christian non-fiction book, "Where the Quiet River Bends." I also want it to promote my web site, www.seedsofrenewalway.com. The book is about empowering people to be transformed through a deeper relationship with God. I am picturing a design with a dove over water that matches the colors of my book cover, blue, white, yellow, and orange. Fire and light would also be possible elements of the design. I would like to be able to use the dove by itself as a logo for my business. This is my first book and I do not know if others will follow. The name of my publishing company is Lantern Valley Press, named after Gideon in the Bible story from the book of Judges. My book was independently published and was recently selected as a finalist for the 2015 Bright Horizon SMALLPRESS book prize in the Christian non-fiction genre.

Target Market(s)

People who are hungry for more of God and who want to experience deep change in their lives.

Industry/Entity Type

Business

Contact Information for Business Card

Dana Whitfield
Author
Where the Quiet River Bends
4283 Maple Hollow Lane
Austin, Texas 78952-1184
512-555-0147 512-555-0193
dana-whitfield@brightmailbox.net
www.seedsofrenewalway.com

Colors
0355a3
3377b5
85acd3
cedeed
fbee3e
ffc214

Requirements
Must have
• A dove with a blue background, peaceful and appealing
Nice to have
• Water and fire or light
Should not have
• Violence or fear-producing images

```html
<!DOCTYPE html>
<html lang="en">
<head>
<meta charset="utf-8">
<title>Lantern Valley Press – Business Card</title>
<link rel="stylesheet" href="https://fonts.googleapis.com/css2?family=Oswald:wght@400;500;700&family=Cinzel:wght@400&family=Great+Vibes&display=swap">
<style>
  :root {
    --stage: #2b2b2d;
    --navy: #1c3d9c;
    --royal: #0355a3;
    --deep: #0d2a7a;
    --sky: #85acd3;
    --mist: #cedeed;
    --orange: #e8542a;
    --ink: #111111;
    --paper: #ffffff;
  }
  * { box-sizing: border-box; margin: 0; padding: 0; }
  html, body { width: 1200px; height: 871px; overflow: hidden; }
  body {
    background: var(--stage);
    position: relative;
    font-family: "Oswald", sans-serif;
  }
  .card {
    position: absolute;
    left: 280px;
    width: 640px;
    height: 366px;
    overflow: hidden;
    box-shadow: 0 10px 30px rgba(0,0,0,.45);
  }

  /* ---------- back side ---------- */
  .card--back {
    top: 40px;
    background: linear-gradient(135deg, var(--royal) 0%, var(--navy) 45%, var(--deep) 100%);
  }
  .card--back .splash {
    position: absolute;
    left: 0; top: 0;
    width: 300px; height: 366px;
    background: radial-gradient(ellipse at 30% 50%, rgba(206,222,237,.55) 0%, rgba(133,172,211,.35) 40%, rgba(3,85,163,0) 75%);
  }
  .book-title {
    position: absolute;
    left: 34px; top: 48px;
    color: var(--mist);
    font-family: "Cinzel", serif;
    font-size: 40px;
    line-height: 46px;
    letter-spacing: 1px;
  }
  .book-title .script {
    display: block;
    font-family: "Great Vibes", cursive;
    font-size: 50px;
    line-height: 58px;
    letter-spacing: 0;
    text-transform: none;
  }
  .back-brand {
    position: absolute;
    left: 330px; top: 120px;
    width: 280px;
    text-align: center;
    color: var(--mist);
  }
  .brand-mark {
    display: block;
    margin: 0 auto 18px;
    width: 56px; height: 56px;
    border-radius: 50%;
    background: var(--mist);
  }
  .back-brand .press-name {
    font-size: 15px;
    letter-spacing: 5px;
    font-weight: 400;
  }
  .back-brand .site {
    margin-top: 14px;
    font-size: 16px;
    letter-spacing: 1.5px;
    font-weight: 500;
  }

  /* ---------- front side ---------- */
  .card--front {
    top: 446px;
    background: var(--paper);
  }
  .front-brand {
    position: absolute;
    left: 26px; top: 110px;
    width: 250px;
    text-align: center;
  }
  .front-brand .brand-mark {
    width: 80px; height: 80px;
    background: var(--navy);
    margin-bottom: 22px;
  }
  .front-brand .press-name {
    color: var(--navy);
    font-size: 15px;
    letter-spacing: 4.5px;
    font-weight: 400;
  }
  .divider {
    position: absolute;
    left: 296px; top: 40px;
    width: 2px; height: 286px;
    background: var(--orange);
  }
  .contact {
    position: absolute;
    left: 318px; top: 44px;
    color: var(--ink);
  }
  .contact .name {
    font-size: 32px;
    font-weight: 700;
    letter-spacing: 1.5px;
    line-height: 40px;
  }
  .contact .role {
    font-size: 15px;
    font-weight: 500;
    color: var(--navy);
    letter-spacing: .5px;
    margin-bottom: 8px;
  }
  .contact .role .label { color: var(--orange); }
  .contact ul { list-style: none; }
  .contact li {
    display: flex;
    align-items: flex-start;
    gap: 10px;
    font-size: 17px;
    font-weight: 500;
    letter-spacing: .8px;
    line-height: 26px;
  }
  .contact .icon {
    flex: 0 0 18px;
    width: 18px; height: 18px;
    margin-top: 4px;
    fill: var(--navy);
  }
</style>
</head>
<body>

  <section class="card card--back" aria-label="Business card, back">
    <div class="splash" role="img" aria-label="Soft watercolour splash texture in pale blue"></div>
    <h1 class="book-title">WHERE THE<br>QUIET<br>RIVER<span class="script">Bends</span></h1>
    <div class="back-brand">
      <span class="brand-mark" aria-hidden="true"></span>
      <p class="press-name">LANTERN VALLEY PRESS</p>
      <p class="site">www.seedsofrenewalway.com</p>
    </div>
  </section>

  <section class="card card--front" aria-label="Business card, front">
    <div class="front-brand">
      <span class="brand-mark" aria-hidden="true"></span>
      <p class="press-name">LANTERN VALLEY PRESS</p>
    </div>
    <div class="divider"></div>
    <div class="contact">
      <h2 class="name">Dana Whitfield</h2>
      <p class="role"><span class="label">Author</span> : Where the Quiet River Bends</p>
      <ul>
        <li>
          <svg class="icon" viewBox="0 0 24 24" aria-hidden="true"><path d="M12 2a7 7 0 0 0-7 7c0 5 7 13 7 13s7-8 7-13a7 7 0 0 0-7-7zm0 9.5A2.5 2.5 0 1 1 12 6.5a2.5 2.5 0 0 1 0 5z"/></svg>
          <span>4283 Maple Hollow Lane Austin<br>Texas 78952-1184</span>
        </li>
        <li>
          <svg class="icon" viewBox="0 0 24 24" aria-hidden="true"><path d="M3 9c0-2 4-4 9-4s9 2 9 4v2h-5V9H8v2H3zM6 12h12l2 7H4z"/></svg>
          <span>512-555-0147</span>
        </li>
        <li>
          <svg class="icon" viewBox="0 0 24 24" aria-hidden="true"><path d="M8 2h8a2 2 0 0 1 2 2v16a2 2 0 0 1-2 2H8a2 2 0 0 1-2-2V4a2 2 0 0 1 2-2zm0 3v13h8V5zm4 14.2a1 1 0 1 0 0 .1z"/></svg>
          <span>512-555-0193</span>
        </li>
        <li>
          <svg class="icon" viewBox="0 0 24 24" aria-hidden="true"><path d="M2 5h20v14H2zm2 2v.5l8 5 8-5V7zm0 3v7h16v-7l-8 5z"/></svg>
          <span>dana-whitfield@brightmailbox.net</span>
        </li>
      </ul>
    </div>
  </section>

</body>
</html>
```